Info Graphic for Real Estate Company

We are Brimlo.com, a real estate company based in Hong Kong. We need a simple info graphic that helps our readers understand more about the property market here. The current topic we are discussing is the difference in the hong kong market in 1997 (market crash) versus the market today. We have very clear direction attached, all of the copy and creative direction. We just need someone to put it in layout! Please see attached :)

Target Market(s)

30-60 year olds; highly educated (investment bankers, lawyers)

Industry/Entity Type

Real Estate

Font styles to use
Other font styles liked:
• Open Sans and Oswald

Colors

Designer to choose colors to be used in the design.

Requirements
Must have
• The attached copy
Nice to have
• A similar design to the attached
Should not have
• colors that do not fall within our guidelines (attached)

```html
<!DOCTYPE html>
<html lang="en">
<head>
<meta charset="utf-8">
<title>Top 5 Differences between 1997 vs. Now</title>
<link href="https://fonts.googleapis.com/css2?family=Oswald:wght@400;500;600;700&family=Open+Sans:wght@400;600&display=swap" rel="stylesheet">
<style>
  :root {
    --maroon: #831a2a;
    --teal: #06898b;
    --gold: #b8930f;
    --white: #ffffff;
    --ink: #222222;
    --badge: #333333;
    --accent-red: #8a1526;
    --page: #efefef;
  }
  * { margin: 0; padding: 0; box-sizing: border-box; }
  html, body { width: 1196px; height: 1200px; overflow: hidden; background: var(--page); }
  .poster {
    position: absolute; left: 173px; top: 0; width: 850px; height: 1200px;
    background: var(--maroon);
  }
  .poster-border {
    position: absolute; left: 16px; top: 13px; right: 16px; bottom: 13px;
    border: 2px dotted rgba(255,255,255,0.85);
  }
  .header {
    position: absolute; left: 40px; top: 24px; width: 772px; height: 355px;
    background: var(--teal); overflow: hidden;
  }
  .header-title {
    position: absolute; top: 12px; left: 0; width: 100%;
    text-align: center; color: var(--white);
    font-family: "Oswald", sans-serif; font-weight: 500; font-size: 29px; line-height: 43px;
  }
  .header-rule {
    position: absolute; top: 107px; left: 96px; width: 578px;
    border-top: 3px dotted var(--white);
  }
  .header-disc {
    position: absolute; left: 260px; top: 124px; width: 214px; height: 214px;
    border-radius: 50%; background: var(--gold);
  }
  .header-top {
    position: absolute; left: 178px; top: 145px; color: var(--white);
    font-family: "Oswald", sans-serif; font-weight: 700; font-size: 92px; line-height: 92px;
    letter-spacing: -2px;
  }
  .header-five {
    position: absolute; left: 318px; top: 130px; color: var(--white);
    font-family: "Oswald", sans-serif; font-weight: 700; font-size: 198px; line-height: 198px;
  }
  .header-sub {
    position: absolute; left: 420px; top: 221px; color: var(--white);
    font-family: "Oswald", sans-serif; font-weight: 500; white-space: nowrap;
  }
  .header-sub .line-a { display: block; font-size: 31px; line-height: 36px; }
  .header-sub .line-b { display: block; font-size: 45px; line-height: 44px; font-weight: 600; }

  .card {
    position: absolute; width: 236px; height: 313px; background: var(--white);
    text-align: center; color: var(--ink);
  }
  .card-icon {
    position: absolute; left: 71px; top: -64px; width: 94px; height: 94px;
    border-radius: 50%; background: var(--gold);
    display: flex; align-items: center; justify-content: center;
  }
  .card-title {
    margin-top: 44px; padding: 0 16px;
    font-family: "Oswald", sans-serif; font-weight: 400; font-size: 18px; line-height: 25px;
  }
  .card-body {
    margin-top: 6px; padding: 0 14px;
    font-family: "Open Sans", sans-serif; font-size: 11.6px; line-height: 16.5px;
  }
  .card-stats { list-style: none; text-align: left; margin-top: 30px; padding: 0 10px; }
  .card-stats li {
    position: relative; padding-left: 13px; margin-bottom: 21px;
    font-family: "Open Sans", sans-serif; font-weight: 600; font-size: 13px; line-height: 19px;
  }
  .card-stats li::before {
    content: ""; position: absolute; left: 1px; top: 7px; width: 5px; height: 5px;
    border-radius: 50%; background: var(--accent-red);
  }
  .card-stats .years { color: var(--accent-red); }
  .card-number {
    position: absolute; left: 94px; bottom: -24px; width: 48px; height: 48px;
    border-radius: 50%; background: var(--badge); color: var(--white);
    outline: 2px dotted var(--badge); outline-offset: 2px;
    font-family: "Oswald", sans-serif; font-weight: 500; font-size: 27px; line-height: 48px;
  }
  .card-1 { left: 33px; top: 452px; }
  .card-2 { left: 307px; top: 452px; }
  .card-3 { left: 583px; top: 452px; }
  .card-4 { left: 174px; top: 841px; }
  .card-5 { left: 441px; top: 841px; }
  .card-1 .card-body, .card-2 .card-body { margin-top: 4px; }
  .card-3 .card-body { padding: 0 16px; }
  .card-4 .card-title { margin-top: 36px; }
  .card-4 .card-body { margin-top: 20px; }
  .card-5 .card-title { margin-top: 30px; }
</style>
</head>
<body>
<main class="poster">
  <div class="poster-border"></div>

  <header class="header">
    <h1 class="header-title">Expert Analysis of Why Hong Kong Real Estate<br>Will Not Crash Like It Did in 1997</h1>
    <div class="header-rule"></div>
    <div class="header-disc"></div>
    <div class="header-top">TOP</div>
    <div class="header-five">5</div>
    <div class="header-sub">
      <span class="line-a">Differences between</span>
      <span class="line-b">1997 VS. NOW</span>
    </div>
  </header>

  <section class="card card-1">
    <div class="card-icon">
      <svg width="60" height="54" viewBox="0 0 60 54" fill="#fff">
        <rect x="22" y="4" width="28" height="18" rx="2"/>
        <rect x="22" y="9" width="28" height="4" fill="#b8930f"/>
        <rect x="26" y="27" width="22" height="4" rx="1"/>
        <rect x="2" y="32" width="9" height="16" rx="1"/>
        <path d="M13 34 h12 c4 0 6 2 6 4 h-12 v3 h14 l14-7 c3-1 5 2 3 4 l-16 11 h-21 z"/>
      </svg>
    </div>
    <h2 class="card-title">Buying has not reached<br>frenzied levels</h2>
    <p class="card-body">Market activity remains<br>close to historical averages</p>
    <ul class="card-stats">
      <li>15-year average <span class="years">(2002-2016)</span><br>= 7,180 transactions/month</li>
      <li>10-year average <span class="years">(2007-2016)</span><br>= 7,150 transactions/month</li>
    </ul>
    <div class="card-number">1</div>
  </section>

  <section class="card card-2">
    <div class="card-icon">
      <svg width="60" height="60" viewBox="0 0 60 60" fill="none" stroke="#fff" stroke-width="7">
        <circle cx="17" cy="16" r="9"/>
        <circle cx="43" cy="44" r="9"/>
        <line x1="48" y1="6" x2="12" y2="54" stroke-linecap="round"/>
      </svg>
    </div>
    <h2 class="card-title">Interest rates<br>are far from risky</h2>
    <p class="card-body">Hong Kong interest rates are approximately 3% (even lower than the 4-5% in most global economies). Going into the crash of 1997, interest rates were over 9%</p>
    <div class="card-number">2</div>
  </section>

  <section class="card card-3">
    <div class="card-icon">
      <svg width="60" height="56" viewBox="0 0 60 56" fill="#fff">
        <rect x="4" y="4" width="26" height="50"/>
        <g fill="#b8930f">
          <rect x="8" y="9" width="7" height="7"/><rect x="19" y="9" width="7" height="7"/>
          <rect x="8" y="20" width="7" height="7"/><rect x="19" y="20" width="7" height="7"/>
          <rect x="8" y="31" width="7" height="7"/><rect x="19" y="31" width="7" height="7"/>
          <rect x="8" y="42" width="7" height="7"/><rect x="19" y="42" width="7" height="7"/>
        </g>
        <rect x="33" y="18" width="6" height="36"/>
        <rect x="33" y="28" width="24" height="26"/>
        <rect x="42" y="38" width="8" height="16" fill="#b8930f"/>
      </svg>
    </div>
    <h2 class="card-title">Affordability –<br>a tale of two cities</h2>
    <p class="card-body">The average property in HK requires 19 years of average income, almost double what it was in 1997. Properties are much less affordable to the average citizen. However, all is not equal, with a lot of pent up demand from people who have held back as a result of government measures and accumulated wealth on the sidelines. The rich have also gotten richer.</p>
    <div class="card-number">3</div>
  </section>

  <section class="card card-4">
    <div class="card-icon">
      <svg width="60" height="56" viewBox="0 0 60 56" fill="#fff">
        <rect x="4" y="4" width="3" height="48"/>
        <rect x="4" y="49" width="52" height="3"/>
        <rect x="11" y="22" width="5" height="27"/>
        <rect x="19" y="30" width="5" height="19"/>
        <circle cx="37" cy="20" r="12" fill="none" stroke="#fff" stroke-width="3"/>
        <text x="37" y="26" text-anchor="middle" font-family="Open Sans, sans-serif" font-weight="600" font-size="16" fill="#fff">$</text>
        <path d="M45 28 l10 14" stroke="#fff" stroke-width="5" stroke-linecap="round"/>
        <rect x="29" y="36" width="5" height="13"/>
      </svg>
    </div>
    <h2 class="card-title">Excess Debt?</h2>
    <p class="card-body">Housing crashes are almost always caused by overleveraging – people borrowing more than they could afford to support when buying a property.&nbsp; The HKMA reported that Hong Kong's average loan-to-value ratio is 51%, lower than the 64% before the cooling measures were introduced. Other global markets typically operate at LTV ratios of 70% or more, and may approach 100% before a housing crash</p>
    <div class="card-number">4</div>
  </section>

  <section class="card card-5">
    <div class="card-icon">
      <svg width="62" height="60" viewBox="0 0 62 60" fill="none" stroke="#fff" stroke-width="3.5" stroke-linejoin="round">
        <path d="M10 24 L31 6 L52 24"/>
        <path d="M16 20 V40 H46 V20"/>
        <rect x="27" y="28" width="8" height="12" fill="#fff"/>
        <path d="M4 44 c8-4 14-2 20 2 h14 c3 0 3 4 0 4 h-12 m12 0 l14-6 c4-2 6 2 3 4 l-15 8 h-36" fill="none"/>
      </svg>
    </div>
    <h2 class="card-title">China – the elephant in the<br>property market</h2>
    <p class="card-body">China is perhaps the most important difference between 1997 and 2017. At the time of the handover, China's economy was just starting its meteoric rise with a GDP of just under US$1 trillion.&nbsp; Over the next 20 years it would grow to over US$11 trillion. There remains tremendous room for mainland Chinese investors to invest in Hong Kong. This did not exist in 1997.</p>
    <div class="card-number">5</div>
  </section>
</main>
</body>
</html>
```